Namecard design for Forex trading & training company

We need a design for a financial forex trading company.
Namecard should give customer a professional yet premium feel, able to differentiate from others.
1) most financial companies employs white background, while its clean and professional, it is too mainstream.
2) I am thinking of brown as base colour, however it easily gives the perception of being an Interior Design company
3) Task is to find a design that is able to portray a clean professional feel, at the same time, appear premium and differentiated from others.
*I'll be employing 3D textured print for my company namecard just so as to give it a better finishing.
Please find attached for my logo.
Financial

```html
<!DOCTYPE html>
<html lang="en">
<head>
<meta charset="utf-8">
<title>Veltrion Capital – Business Card</title>
<link rel="stylesheet" href="https://fonts.googleapis.com/css2?family=Libre+Baskerville&family=Open+Sans&display=swap">
<style>
  :root {
    --backdrop: #ecd3a6;
    --wood-dark: #2e150c;
    --wood-mid: #5a2c16;
    --wood-light: #6e3a1d;
    --panel: #170d0d;
    --panel-rim: #0b0303;
    --ink-light: #ffffff;
    --brand-blue: #5a5fa8;
  }
  html, body {
    margin: 0;
    width: 1189px;
    height: 1200px;
    overflow: hidden;
    background: var(--backdrop);
  }
  .canvas {
    position: relative;
    width: 1189px;
    height: 1200px;
  }
  .card {
    position: absolute;
    left: 171px;
    width: 856px;
    height: 488px;
    overflow: hidden;
  }
  .card--front { top: 68px; }
  .card--back { top: 627px; }
  .card__wood {
    position: absolute;
    inset: 0;
    background:
      radial-gradient(ellipse at 50% 50%, var(--wood-light) 0%, transparent 70%),
      linear-gradient(180deg, var(--wood-dark) 0%, var(--wood-mid) 25%, var(--wood-dark) 50%, var(--wood-mid) 78%, var(--wood-dark) 100%);
  }
  .card__panel {
    position: absolute;
    left: 83px;
    top: 47px;
    width: 690px;
    height: 393px;
    box-sizing: border-box;
    border-radius: 196px;
    background: var(--panel);
    border: 18px solid var(--panel-rim);
    box-shadow: inset 0 0 12px rgba(0,0,0,0.8);
  }
  .brand-name {
    position: absolute;
    left: 0;
    right: 0;
    top: 228px;
    margin: 0;
    text-align: center;
    font-family: "Libre Baskerville", serif;
    font-size: 26px;
    letter-spacing: 0.32em;
    padding-left: 0.32em;
    color: var(--brand-blue);
    font-weight: 400;
  }
  .contact {
    position: absolute;
    inset: 0;
    color: var(--ink-light);
    text-align: center;
  }
  .contact__name {
    position: absolute;
    left: 0; right: 0; top: 127px;
    margin: 0;
    font-family: "Libre Baskerville", serif;
    font-size: 30px;
    font-weight: 400;
  }
  .contact__role {
    position: absolute;
    left: 0; right: 0; top: 162px;
    margin: 0;
    font-family: "Libre Baskerville", serif;
    font-size: 19px;
  }
  .contact__rule {
    position: absolute;
    left: 219px;
    width: 418px;
    height: 2px;
    background: var(--ink-light);
  }
  .contact__rule--top { top: 216px; }
  .contact__rule--bottom { top: 313px; }
  .contact__line {
    position: absolute;
    left: 0; right: 0;
    margin: 0;
    font-family: "Open Sans", sans-serif;
    font-size: 22px;
    display: flex;
    justify-content: center;
    align-items: center;
    gap: 12px;
  }
  .contact__line--phone { top: 230px; }
  .contact__line--email { top: 267px; }
  .contact__line--web { top: 329px; }
  .icon { width: 20px; height: 20px; fill: var(--ink-light); }
</style>
</head>
<body>
<main class="canvas">
  <section class="card card--front">
    <div class="card__wood" role="img" aria-label="Dark brown wood grain texture"></div>
    <div class="card__panel"></div>
    <h1 class="brand-name">VELTRION CAPITAL</h1>
  </section>

  <section class="card card--back">
    <div class="card__wood" role="img" aria-label="Dark brown wood grain texture"></div>
    <div class="card__panel"></div>
    <div class="contact">
      <h2 class="contact__name">Marcus Lee</h2>
      <p class="contact__role">Pantry Manager</p>
      <div class="contact__rule contact__rule--top"></div>
      <p class="contact__line contact__line--phone">
        <svg class="icon" viewBox="0 0 20 20" aria-hidden="true"><rect x="5" y="1" width="10" height="18" rx="2"/><rect x="7" y="3" width="6" height="6" fill="#170d0d"/></svg>
        (86) 555 010 234
      </p>
      <p class="contact__line contact__line--email">
        <svg class="icon" viewBox="0 0 20 20" aria-hidden="true"><rect x="1" y="4" width="18" height="12"/><path d="M1 4 L10 11 L19 4" stroke="#170d0d" stroke-width="1.5" fill="none"/><path d="M1 16 L8 9.5 M19 16 L12 9.5" stroke="#170d0d" stroke-width="1.5"/></svg>
        Marcus@veltrioncap.com
      </p>
      <div class="contact__rule contact__rule--bottom"></div>
      <p class="contact__line contact__line--web">www.veltrioncap.com</p>
    </div>
  </section>
</main>
</body>
</html>
```